Business software developers new website

We need to redesign our website. Our current website is http://www.plumvista.net/index.html, which is outdated and needs a new look. We moved out from web design and have concentrated more on the back end of the systems, for example, system support and security and cloud-based applications. Our major clients include both private and government sectors. We would like to see some designs that are all in one page, simple and clean. Prefer illustrator or obstructed images instead of real-life photos. Must look futuristic yet friendly. Attached the new logo for your references and good luck.

Target Market(s)

Medium to big company for their IT or data management. Either improve or upgrade their current system.

Industry/Entity Type

Business Software

Number of Pages Required

1 page

Colors

Designer to choose colors to be used in the design.

Requirements
Must have
• Simple and clean. Individual assets must be provided in the correct size and format(png or jpeg). Prefer Goggle fonts. Even though the logo color is red, grey and black, still prefer some modern colors that go well with red. When design, must consider the possibility to convert it into responsive.
Nice to have
• White background
Should not have
• real life photos, no slider

```html
<!DOCTYPE html>
<html lang="en">
<head>
<meta charset="utf-8">
<title>PlumVista — Business Software</title>
<link href="https://fonts.googleapis.com/css2?family=Montserrat:wght@400;500;600;700;800&family=Open+Sans:wght@400;600&display=swap" rel="stylesheet">
<style>
:root{
  --red:#e8203a;
  --red-soft:#ff5b4f;
  --ink:#111216;
  --text:#5d6068;
  --muted:#9a9ca3;
  --line:#d9dbe0;
  --blue:#3f6fe8;
  --blue-soft:#a9c3ff;
  --white:#ffffff;
  --footer:#6d6f74;
}
*{margin:0;padding:0;box-sizing:border-box}
html,body{width:1200px;height:3304px;overflow:hidden;background:var(--white)}
body{position:relative;font-family:"Open Sans",Arial,sans-serif;color:var(--text);font-size:13px;line-height:1.6}
.abs{position:absolute}
h1,h2,h3,h4,.brand,.nav a,.btn{font-family:"Montserrat",Arial,sans-serif}
.section-title{position:absolute;font-size:30px;font-weight:700;color:var(--ink);line-height:1.2}
.section-title::after{content:"";display:block;width:96px;height:4px;background:var(--red);margin-top:8px;border-radius:2px}
.art{position:absolute;border-radius:24px}
.read-more{color:var(--red);font-size:11px;font-weight:600;display:block;margin-top:6px}

/* top bar */
.topbar{left:232px;top:10px;display:flex;gap:30px;font-size:11px;color:var(--text);align-items:center}
.topbar span{display:flex;align-items:center;gap:6px}
.topbar svg{width:12px;height:12px}
.brand{font-size:22px;font-weight:700;color:var(--ink);letter-spacing:-.3px}
.header-brand{left:232px;top:40px}
.nav{right:228px;top:46px;display:flex;gap:26px}
.nav a{font-size:12px;font-weight:600;color:var(--ink);text-decoration:none;letter-spacing:.5px}
.nav a.active{border-bottom:2px solid var(--red);padding-bottom:4px}

/* hero */
.hero-title{left:232px;top:160px;width:460px;font-size:48px;font-weight:700;color:var(--ink);line-height:1.22}
.btn{display:inline-block;background:var(--red);color:var(--white);font-size:11px;font-weight:600;letter-spacing:1px;border-radius:22px;padding:12px 28px}
.hero-btn{left:232px;top:330px}
.hero-art{left:690px;top:80px;width:490px;height:420px;border-radius:48% 52% 40% 60%;background:radial-gradient(circle at 40% 40%,var(--blue-soft),var(--blue) 45%,var(--red-soft) 70%,var(--red))}

/* services */
.services-art{left:70px;top:700px;width:320px;height:300px;background:linear-gradient(135deg,#e4ecff,var(--blue) 60%,var(--red))}
.services-grid{left:420px;top:700px;width:580px;display:grid;grid-template-columns:repeat(3,1fr);column-gap:40px;row-gap:50px}
.service svg{width:30px;height:30px;margin-bottom:8px}
.service h3{font-size:13px;font-weight:700;color:var(--ink);margin-bottom:4px}
.service p{font-size:11px;line-height:1.55;color:var(--muted)}

/* about */
.about-text{left:232px;top:1200px;width:560px;font-size:13px;color:var(--muted)}
.about-art{left:800px;top:1060px;width:380px;height:300px;background:linear-gradient(135deg,#ffd8b0,var(--blue) 55%,var(--blue-soft))}

/* testimonials */
.testi-art{left:210px;top:1420px;width:280px;height:270px;background:linear-gradient(160deg,#ffd0d6,var(--red-soft) 50%,var(--blue))}
.testi-text{left:608px;top:1580px;width:440px;font-size:13px;color:var(--muted)}
.testi-name{color:var(--red);font-weight:600;font-size:12px;margin-top:10px}

/* clients */
.clients{left:232px;top:1890px;display:flex;gap:68px}
.client{width:120px}
.client-mark{height:60px;display:flex;align-items:center;font-family:"Montserrat",Arial,sans-serif;font-size:18px;font-weight:700;color:var(--ink)}
.client small{display:block;font-size:11px;color:var(--muted);margin-top:6px}
.clients-art{left:830px;top:1728px;width:340px;height:310px;background:linear-gradient(150deg,#bfe9e4,var(--blue-soft) 45%,var(--blue))}

/* pricing */
.pricing-lead{left:232px;top:2192px;width:520px;font-size:12px;color:var(--muted)}
.plans{left:232px;top:2248px;display:flex;gap:16px}
.plan{width:268px;height:316px;background:var(--ink);color:var(--white);text-align:center;padding:26px 22px}
.plan.featured{background:var(--red)}
.plan h4{font-size:11px;font-weight:600;letter-spacing:1px;text-transform:uppercase;margin-bottom:4px}
.plan .plan-sub{font-size:10px;opacity:.7;margin-bottom:20px}
.plan .price{font-family:"Montserrat",Arial,sans-serif;font-size:52px;font-weight:700;line-height:1}
.plan .price sup{font-size:22px;vertical-align:top;position:relative;top:6px}
.plan .period{font-size:10px;letter-spacing:1px;opacity:.8;margin:8px 0 18px}
.plan ul{list-style:none;font-size:11px;opacity:.85;line-height:1.8;margin-bottom:22px}
.plan .btn-outline{display:inline-block;border:1px solid var(--white);border-radius:20px;padding:9px 26px;font-family:"Montserrat",Arial,sans-serif;font-size:10px;font-weight:600;letter-spacing:1px}

/* contact */
.contact-form{left:232px;top:2740px;width:410px}
.field{border-bottom:1px solid var(--line);font-size:11px;color:var(--muted);padding-bottom:16px;margin-bottom:24px}
.field.message{height:70px}
.contact-btn{margin-top:8px;background:var(--ink)}
.contact-art{left:740px;top:2720px;width:320px;height:360px;background:linear-gradient(160deg,#e6ecff,var(--blue) 60%,var(--red))}

/* footer */
.footer-brand{left:0;width:1200px;top:3102px;text-align:center}
.footer-links{left:0;width:1200px;top:3150px;text-align:center;font-size:11px;color:var(--text)}
.footer-links span{margin:0 6px}
.socials{left:0;width:1200px;top:3190px;display:flex;justify-content:center;gap:20px}
.socials i{width:12px;height:12px;border-radius:50%;background:var(--ink);display:block}
.bottom-bar{left:0;top:3262px;width:1200px;height:42px;background:var(--footer);color:#e9e9ea;font-size:10px;display:flex;justify-content:space-between;align-items:center;padding:0 232px}
</style>
</head>
<body>

<header>
  <div class="abs topbar">
    <span><svg viewBox="0 0 24 24"><path fill="#e8203a" d="M6.6 10.8a15 15 0 0 0 6.6 6.6l2.2-2.2c.3-.3.7-.4 1-.2 1.1.4 2.3.6 3.6.6.6 0 1 .4 1 1V20c0 .6-.4 1-1 1C10.6 21 3 13.4 3 4c0-.6.4-1 1-1h3.5c.6 0 1 .4 1 1 0 1.3.2 2.5.6 3.6.1.3 0 .7-.2 1z"/></svg>+1 555 014 2880</span>
    <span><svg viewBox="0 0 24 24"><rect x="2" y="5" width="20" height="14" rx="2" fill="#e8203a"/><path d="M3 6l9 7 9-7" stroke="#fff" stroke-width="1.5" fill="none"/></svg>hello@plumvista.net</span>
  </div>
  <div class="abs brand header-brand">plumvista.net</div>
  <nav class="abs nav">
    <a class="active">HOME</a><a>ABOUT</a><a>SERVICES</a><a>PRICE</a><a>CONTACTS</a>
  </nav>
</header>

<section class="hero">
  <h1 class="abs hero-title">Create stories for the digital corporate</h1>
  <span class="abs btn hero-btn">READ ABOUT US</span>
  <div class="art hero-art" role="img" aria-label="Illustration of people building a large web page screen with charts"></div>
</section>

<section class="services">
  <h2 class="section-title" style="left:420px;top:620px">What We Do</h2>
  <div class="art services-art" role="img" aria-label="Illustration of a browser window with code panels and a gear"></div>
  <div class="abs services-grid">
    <div class="service">
      <svg viewBox="0 0 30 30"><rect x="3" y="5" width="24" height="18" rx="2" fill="none" stroke="#e8203a" stroke-width="2"/><path d="M3 10h24" stroke="#3f6fe8" stroke-width="2"/></svg>
      <h3>Web Design</h3>
      <p>Clean, modern layouts planned around your users and business goals from day one.</p>
      <span class="read-more">Read More</span>
    </div>
    <div class="service">
      <svg viewBox="0 0 30 30"><path d="M11 9l-6 6 6 6M19 9l6 6-6 6" fill="none" stroke="#3f6fe8" stroke-width="2.4"/></svg>
      <h3>Software Development</h3>
      <p>Reliable back end systems built to scale with your data and your teams.</p>
      <span class="read-more">Read More</span>
    </div>
    <div class="service">
      <svg viewBox="0 0 30 30"><rect x="5" y="16" width="4" height="9" fill="#e8203a"/><rect x="13" y="11" width="4" height="14" fill="#3f6fe8"/><rect x="21" y="6" width="4" height="19" fill="#e8203a"/></svg>
      <h3>Marketing</h3>
      <p>Clear digital strategy that brings the right clients to your services.</p>
      <span class="read-more">Read More</span>
    </div>
    <div class="service">
      <svg viewBox="0 0 30 30"><circle cx="15" cy="15" r="6" fill="none" stroke="#e8203a" stroke-width="2.4"/><path d="M15 3v5M15 22v5M3 15h5M22 15h5" stroke="#3f6fe8" stroke-width="2.4"/></svg>
      <h3>Programming</h3>
      <p>Custom modules written in modern languages for secure, stable results.</p>
      <span class="read-more">Read More</span>
    </div>
    <div class="service">
      <svg viewBox="0 0 30 30"><path d="M15 3l10 4v7c0 6-4 11-10 13C9 25 5 20 5 14V7z" fill="none" stroke="#3f6fe8" stroke-width="2.2"/><path d="M10 15l4 4 6-7" fill="none" stroke="#e8203a" stroke-width="2.2"/></svg>
      <h3>B2C Compliance</h3>
      <p>Security reviews and support that keep your systems safe and up to standard.</p>
      <span class="read-more">Read More</span>
    </div>
    <div class="service">
      <svg viewBox="0 0 30 30"><path d="M8 22h15a5 5 0 0 0 0-10 7 7 0 0 0-13-1A5.5 5.5 0 0 0 8 22z" fill="none" stroke="#e8203a" stroke-width="2.2"/></svg>
      <h3>Hosting Solutions</h3>
      <p>Cloud based hosting with steady uptime and monitoring around the clock.</p>
      <span class="read-more">Read More</span>
    </div>
  </div>
</section>

<section class="about">
  <h2 class="section-title" style="left:232px;top:1120px">About Us</h2>
  <p class="abs about-text">We are a small team of engineers focused on back end systems, support, security and cloud based applications. For years we have helped private firms and government bodies improve and upgrade the systems they rely on every day, with care and clear communication.</p>
  <div class="art about-art" role="img" aria-label="Illustration of a person on a ladder arranging chat and data panels"></div>
</section>

<section class="testimonials">
  <div class="art testi-art" role="img" aria-label="Illustration of a person holding a magnet that attracts hearts"></div>
  <h2 class="section-title" style="left:608px;top:1500px">Testimonials</h2>
  <div class="abs testi-text">
    <p>"The team moved our records to the cloud without a single lost day. Support is quick, friendly and always clear. We feel our data is safer than ever and our staff can finally focus on their own work."</p>
    <p class="testi-name">Jordan Elms, IT Lead</p>
  </div>
</section>

<section class="clients-section">
  <h2 class="section-title" style="left:232px;top:1800px">Our Clients</h2>
  <div class="abs clients">
    <div class="client"><div class="client-mark">Northwind</div><small>Logistics Group</small></div>
    <div class="client"><div class="client-mark">Bayline</div><small>Public Services</small></div>
    <div class="client"><div class="client-mark">Kestrel</div><small>Retail Partner</small></div>
  </div>
  <div class="art clients-art" role="img" aria-label="Illustration of a laptop connected to a cloud with people at work"></div>
</section>

<section class="pricing">
  <h2 class="section-title" style="left:232px;top:2124px">Pricing Table</h2>
  <p class="abs pricing-lead">Simple monthly plans for hosting, support and security. Pick the level that fits your team today and upgrade at any time.</p>
  <div class="abs plans">
    <div class="plan">
      <h4>Web Hosting Starter</h4>
      <p class="plan-sub">Best for small teams</p>
      <div class="price"><sup>$</sup>39</div>
      <p class="period">MONTHLY</p>
      <ul><li>10 GB cloud storage</li><li>Email support included</li></ul>
      <span class="btn-outline">GET STARTED</span>
    </div>
    <div class="plan featured">
      <h4>Web Pro</h4>
      <p class="plan-sub">Best for growing firms</p>
      <div class="price"><sup>$</sup>69</div>
      <p class="period">MONTHLY</p>
      <ul><li>50 GB cloud storage</li><li>Priority support included</li></ul>
      <span class="btn-outline">GET STARTED</span>
    </div>
    <div class="plan">
      <h4>Enterprise Plan</h4>
      <p class="plan-sub">Best for large groups</p>
      <div class="price"><sup>$</sup>89</div>
      <p class="period">MONTHLY</p>
      <ul><li>Unlimited cloud storage</li><li>Dedicated security team</li></ul>
      <span class="btn-outline">GET STARTED</span>
    </div>
  </div>
</section>

<section class="contact">
  <h2 class="section-title" style="left:232px;top:2668px">Contact Us</h2>
  <form class="abs contact-form">
    <div class="field">Full Name</div>
    <div class="field">Email</div>
    <div class="field message">Message</div>
    <span class="btn contact-btn">SEND MESSAGE</span>
  </form>
  <div class="art contact-art" role="img" aria-label="Illustration of two people shaking hands on a paper plane"></div>
</section>

<footer>
  <div class="abs brand footer-brand">plumvista.net</div>
  <div class="abs footer-links"><span>Terms of Use</span>|<span>Terms of Sale</span>|<span>Privacy Policy</span>|<span>Cookie Policy</span></div>
  <div class="abs socials"><i></i><i></i><i></i><i></i></div>
  <div class="abs bottom-bar"><span>© 2024 plumvista.net. All rights reserved.</span><span>Business Software Solutions</span></div>
</footer>

</body>
</html>
```